Verpackungen für Glückskekse
Zielgruppe
Wir sind ein Produzent für regionale Glückskekse aus Niederbayern. Unsere Zielgruppe sind hauptsächlich Frauen zwischen 25 und 55, da unsere Glückskekse hauptsächlich als Gastgeschenke für Hochzeiten, Taufen und Geburtstage verwendet werden.
Aufgabenstellung
Das Vektor Design ist für eine Kartonbox in 12x12x12cm für 12 einzeln verpackte Glückskekse. Auf der Box und auf den Glückskeksen soll der Spruch 'Schön, dass du da bist' stehen.
Primär sollen die Glückskekse auf Hochzeiten eingesetzt werden, die im Boho/Beige-Weiß/Pampasgras Stil dekoriert sind.
Ich habe bereits einen ersten Entwurf, bin mir aber dabei noch nicht ganz sicher. Deshalb sollte der Vorschlag nur als Anhaltspunkt gesehen werden. Gerne auch eigene Ideen anbieten.

```html
<!DOCTYPE html>
<html lang="de">
<head>
<meta charset="utf-8">
<title>Glückskeks-Box – Schön, dass du da bist</title>
<link rel="stylesheet" href="https://fonts.googleapis.com/css2?family=Caveat:wght@400&family=Mrs+Saint+Delafield&display=swap">
<style>
  :root {
    --page: #ffffff;
    --panel-front: #ffffff;
    --panel-side: #f8f3f0;
    --panel-line: #d9d4d1;
    --ink: #4a3b33;
    --frame: #4a4542;
    --heart: #2f2f2c;
    --pampas: #d9b594;
    --pampas-light: #efdfce;
    --blossom: #ecc3c0;
    --pearl: #f4ebdf;
  }
  * { margin: 0; padding: 0; box-sizing: border-box; }
  html, body {
    width: 1200px; height: 848px; overflow: hidden;
    background: var(--page);
  }
  .sheet { position: relative; width: 1200px; height: 848px; }
  .box-face {
    position: absolute; top: 182px; width: 487px; height: 487px;
    border: 1px solid var(--panel-line);
    overflow: hidden;
  }
  .box-face--front { left: 113px; background: var(--panel-front); }
  .box-face--side { left: 599px; background: var(--panel-side); border-left: none; }
  .face-art { position: absolute; inset: 0; width: 100%; height: 100%; }
  .slogan {
    position: absolute; color: var(--ink); line-height: 1; white-space: nowrap;
  }
  .slogan__main {
    top: 176px; left: 166px;
    font-family: "Mrs Saint Delafield", cursive;
    font-size: 84px;
  }
  .slogan__sub {
    top: 246px; left: 168px;
    font-family: "Caveat", cursive;
    font-size: 30px;
    letter-spacing: 0.5px;
    transform: rotate(-2deg);
    transform-origin: left center;
  }
</style>
</head>
<body>
<main class="sheet">

  <section class="box-face box-face--front">
    <svg class="face-art" viewBox="0 0 487 487">
      <defs>
        <linearGradient id="bouquetTone" x1="0" y1="0" x2="1" y2="1">
          <stop offset="0%" stop-color="var(--pampas-light)"/>
          <stop offset="35%" stop-color="var(--pampas)"/>
          <stop offset="60%" stop-color="var(--blossom)"/>
          <stop offset="100%" stop-color="var(--pearl)"/>
        </linearGradient>
      </defs>
      <g class="frame" fill="none" stroke="var(--frame)" stroke-width="0.9">
        <polygon points="249,99 300,110 362,175 368,250 340,330 300,360 249,370 170,362 125,318 108,240 130,160 190,110"/>
        <polygon points="232,108 322,122 378,196 366,300 316,352 230,368 150,346 118,280 124,190 170,132"/>
      </g>
      <path role="img" aria-label="Aquarell-Bouquet aus Pampasgras, rosa Blüten und Perlkugeln, oben links am Rahmen"
            fill="url(#bouquetTone)" opacity="0.8"
            d="M20 90 C60 40 160 50 260 70 C230 110 200 130 150 150 C130 200 150 260 150 300 C110 300 60 290 45 260 C20 200 50 150 20 90 Z"/>
      <path role="img" aria-label="Aquarell-Bouquet aus Pampasgras, rosa Blüten und Perlkugeln, unten rechts am Rahmen"
            fill="url(#bouquetTone)" opacity="0.8"
            d="M360 140 C430 160 470 250 450 320 C420 370 360 420 320 450 C300 400 290 380 230 370 C290 360 330 320 330 280 C320 230 320 180 360 140 Z"/>
      <path class="heart" fill="var(--heart)" d="M169 186 c-6-5-12-9-12-15 a6 6 0 0 1 12-2 a6 6 0 0 1 12 2 c0 6-6 10-12 15z"/>
    </svg>
    <p class="slogan slogan__main">Schön,</p>
    <p class="slogan slogan__sub">dass du da bist!</p>
  </section>

  <section class="box-face box-face--side">
    <svg class="face-art" viewBox="0 0 487 487">
      <defs>
        <linearGradient id="bouquetToneSide" x1="0" y1="1" x2="1" y2="0">
          <stop offset="0%" stop-color="var(--pampas)"/>
          <stop offset="40%" stop-color="var(--blossom)"/>
          <stop offset="65%" stop-color="var(--pearl)"/>
          <stop offset="100%" stop-color="var(--pampas-light)"/>
        </linearGradient>
      </defs>
      <path role="img" aria-label="Aquarell-Bouquet aus Pampasgras, rosa Blüten und Perlkugeln"
            fill="url(#bouquetToneSide)" opacity="0.8"
            d="M45 280 C120 250 180 230 230 170 C260 120 320 80 380 80 C360 150 400 190 440 230 C380 250 330 300 300 330 C260 370 180 400 150 400 C170 350 140 320 45 280 Z"/>
      <path class="heart" fill="var(--heart)" d="M164 186 c-6-5-12-9-12-15 a6 6 0 0 1 12-2 a6 6 0 0 1 12 2 c0 6-6 10-12 15z"/>
    </svg>
  </section>

</main>
</body>
</html>
```